Business Postcard Mailer - 2 sided - 6 x 10.5 inches

We will be purchasing multiple designs through this project. We need a postcard mailer for a residential painting business. The final design needs to have the special 15% Off, contact information, company logo, stamp indicia, and list of services. I will provide past examples and any additional logos. Company colors are #34482E and #4A1717. Old samples are provided. Final flat size should be 6 x 10.5 inches. And we will need a return address in the upper left-hand corner of the backside. QMRB Layout Guidelines are attached. 4389 Juniper Ave #7, Waukesha, WI 53947.
Updates

I just guaranteed the project and will be expecting more entries. We will also be purchasing additional designs (4-5) so we want to ensure a good variety.

Target Market(s)

Homeowners

Industry/Entity Type

Painting

Font styles to use
Sans Serif

Requirements
Must have
• Logo and brand colors
Nice to have
• Call to action - Book your free estimate at www.BrightCoatCrew.example or Call now 262-555-0147.

```html
<!DOCTYPE html>
<html lang="en">
<head>
<meta charset="UTF-8">
<title>BrightCoat Crew – Postcard Mailer</title>
<link href="https://fonts.googleapis.com/css2?family=Open+Sans:wght@400;600;700;800&display=swap" rel="stylesheet">
<style>
  :root {
    --brand-green: #34482E;
    --brand-maroon: #4A1717;
    --ink: #222222;
    --muted: #555555;
    --panel: #e9e9ea;
    --page: #efefef;
    --paper: #ffffff;
  }
  * { box-sizing: border-box; margin: 0; padding: 0; }
  html, body { width: 1200px; height: 1200px; overflow: hidden; }
  body { background: var(--page); font-family: 'Open Sans', Arial, sans-serif; color: var(--ink); position: relative; }

  .card { position: absolute; left: 100px; width: 1000px; height: 571px; background: var(--paper); overflow: hidden; box-shadow: 0 2px 8px rgba(0,0,0,.12); }
  .card--front { top: 20px; }
  .card--back { top: 609px; }

  /* ---------- FRONT ---------- */
  .hero-photo { position: absolute; left: 0; top: 0; width: 640px; height: 420px;
    background: linear-gradient(100deg, #f3f0ec 0%, #d9d3cc 22%, #b7a08a 45%, #8a6a3f 65%, #a46a2a 85%, #5b4a32 100%); }
  .hero-fade { position: absolute; left: 0; top: 0; width: 330px; height: 260px;
    background: linear-gradient(135deg, rgba(255,255,255,.95) 0%, rgba(255,255,255,.75) 55%, rgba(255,255,255,0) 100%); }
  .brand { position: absolute; left: 40px; top: 80px; display: flex; align-items: center; gap: 12px; }
  .brand__mark { width: 22px; height: 22px; background: var(--brand-green); }
  .brand__name { font-weight: 800; font-size: 44px; line-height: 1; color: var(--brand-green); letter-spacing: -0.5px; }

  .ribbon-clip { position: absolute; left: 0; top: 0; width: 640px; height: 420px; overflow: hidden; z-index: 2; }
  .ribbon { position: absolute; left: 455px; top: 40px; width: 260px; height: 50px; background: #1f1f1f; transform: rotate(38deg);
    color: #fff; font-size: 14px; font-weight: 600; line-height: 1.15; text-align: center; padding-top: 7px; }

  .staff-photo { position: absolute; left: 640px; top: 0; width: 360px; height: 330px;
    background: linear-gradient(180deg, #ececec 0%, #d6d2cf 40%, #b59c90 70%, #e3e3e3 100%); }
  .services { position: absolute; left: 640px; top: 330px; width: 360px; height: 175px; background: var(--panel); padding: 18px 0 0 50px; list-style: none; }
  .services li { display: flex; align-items: center; gap: 8px; font-size: 19px; font-weight: 600; color: var(--ink); line-height: 27px; white-space: nowrap; }
  .tick { width: 15px; height: 15px; flex: none; }

  .detail-photo { position: absolute; left: 0; top: 420px; width: 270px; height: 85px;
    background: linear-gradient(90deg, #6b4a2c 0%, #a9876a 45%, #d8cbbb 100%); }
  .offer { position: absolute; left: 270px; top: 395px; width: 370px; height: 110px; background: var(--brand-maroon); color: #fff; padding: 14px 18px 0 22px; }
  .offer__row { display: flex; align-items: center; gap: 14px; white-space: nowrap; }
  .offer__label { font-weight: 800; font-size: 19px; line-height: 20px; text-transform: uppercase; }
  .offer__value { font-weight: 800; font-size: 48px; line-height: 54px; letter-spacing: 1px; }
  .offer__note { font-size: 15px; letter-spacing: 1px; margin-top: 8px; white-space: nowrap; }

  .front-footer { position: absolute; left: 0; top: 505px; width: 1000px; height: 66px; display: flex; align-items: center; padding: 0 30px; gap: 18px; white-space: nowrap; }
  .web { display: flex; align-items: center; gap: 12px; font-size: 30px; color: var(--brand-green); font-weight: 700; }
  .web small { font-size: 22px; font-weight: 400; color: var(--ink); }
  .sep-dot { width: 8px; height: 8px; border-radius: 50%; background: #aaa; }
  .call { display: flex; align-items: center; gap: 10px; font-size: 28px; color: var(--ink); }
  .call strong { color: var(--brand-green); font-weight: 700; font-size: 32px; }
  .icon { fill: none; stroke: #888; stroke-width: 2; }

  /* ---------- BACK ---------- */
  .return-address { position: absolute; left: 40px; top: 30px; font-size: 14px; line-height: 1.35; color: var(--ink); font-style: normal; }
  .return-address strong { display: block; font-size: 17px; font-weight: 800; color: var(--brand-green); }
  .indicia { position: absolute; left: 880px; top: 30px; width: 90px; height: 86px; border: 2px solid #222; text-align: center; font-size: 10px; line-height: 1.2; padding-top: 8px; }
  .indicia b { display: block; font-size: 13px; margin: 4px 0 3px; border-bottom: 1px solid #222; border-top: 1px solid #222; }
  .address-window { position: absolute; left: 560px; top: 150px; width: 410px; height: 210px; border: 1.5px solid #9a9a9a; border-radius: 14px; }
  .intro { position: absolute; left: 40px; top: 200px; width: 430px; font-size: 14px; line-height: 1.4; color: var(--ink); }
  .values { position: absolute; left: 40px; top: 300px; list-style: none; }
  .values li { display: flex; align-items: center; gap: 8px; font-size: 15px; font-weight: 700; text-transform: uppercase; line-height: 26px; }
  .info { position: absolute; left: 560px; top: 385px; width: 420px; display: flex; gap: 12px; align-items: center; font-size: 14px; line-height: 1.35; }
  .info svg { flex: none; }
  .back-band { position: absolute; left: 0; top: 470px; width: 1000px; height: 101px; background: var(--brand-green); }
  .cta-tab { position: absolute; left: 370px; top: 445px; width: 280px; height: 34px; background: var(--brand-maroon); color: #fff;
    font-size: 14px; font-weight: 700; letter-spacing: 1px; text-align: center; line-height: 34px; clip-path: polygon(4% 0, 96% 0, 100% 100%, 0 100%); }
  .band-row { position: absolute; left: 30px; right: 30px; top: 508px; display: flex; align-items: center; justify-content: space-between; color: #fff; font-size: 16px; white-space: nowrap; }
  .band-row .band-brand { font-weight: 800; font-size: 17px; }
  .band-row .item { display: flex; align-items: center; gap: 8px; }
  .band-row .item b { font-weight: 700; }
  .band-row .dot { width: 6px; height: 6px; border-radius: 50%; background: #fff; flex: none; }
  .icon--light { fill: none; stroke: #fff; stroke-width: 2; }
</style>
</head>
<body>

<section class="card card--front" aria-label="Postcard front">
  <div class="hero-photo" role="img" aria-label="Photo of a two-storey stone house being repainted among autumn trees"></div>
  <div class="hero-fade"></div>
  <div class="brand">
    <span class="brand__mark"></span>
    <span class="brand__name">BrightCoat Crew</span>
  </div>
  <div class="ribbon-clip"><div class="ribbon">Locally owned<br>&amp; operated</div></div>

  <div class="staff-photo" role="img" aria-label="Photo of a smiling painter in overalls holding colour swatches"></div>
  <ul class="services">
    <li><svg class="tick" viewBox="0 0 16 16"><rect x="1" y="3" width="11" height="11" fill="none" stroke="#222" stroke-width="1.5"/><path d="M4 8l3 3 8-9" fill="none" stroke="#222" stroke-width="2"/></svg>Interior Painting</li>
    <li><svg class="tick" viewBox="0 0 16 16"><rect x="1" y="3" width="11" height="11" fill="none" stroke="#222" stroke-width="1.5"/><path d="M4 8l3 3 8-9" fill="none" stroke="#222" stroke-width="2"/></svg>Exterior Painting</li>
    <li><svg class="tick" viewBox="0 0 16 16"><rect x="1" y="3" width="11" height="11" fill="none" stroke="#222" stroke-width="1.5"/><path d="M4 8l3 3 8-9" fill="none" stroke="#222" stroke-width="2"/></svg>Carpentry Services</li>
    <li><svg class="tick" viewBox="0 0 16 16"><rect x="1" y="3" width="11" height="11" fill="none" stroke="#222" stroke-width="1.5"/><path d="M4 8l3 3 8-9" fill="none" stroke="#222" stroke-width="2"/></svg>Drywall Repair</li>
    <li><svg class="tick" viewBox="0 0 16 16"><rect x="1" y="3" width="11" height="11" fill="none" stroke="#222" stroke-width="1.5"/><path d="M4 8l3 3 8-9" fill="none" stroke="#222" stroke-width="2"/></svg>Color Consultations</li>
  </ul>

  <div class="detail-photo" role="img" aria-label="Photo of a painter brushing wooden trim"></div>
  <div class="offer">
    <div class="offer__row">
      <span class="offer__label">Spring<br>Special</span>
      <span class="offer__value">15% OFF</span>
    </div>
    <p class="offer__note">Starting March, Interior &amp; Exterior</p>
  </div>

  <div class="front-footer">
    <div class="web">
      <svg width="30" height="30" viewBox="0 0 30 30" class="icon"><circle cx="15" cy="15" r="12"/><ellipse cx="15" cy="15" rx="5" ry="12"/><path d="M3 15h24M5 9h20M5 21h20"/></svg>
      <span><small>www.</small>BrightCoatCrew<small>.example</small></span>
    </div>
    <span class="sep-dot"></span>
    <div class="call">
      <svg width="26" height="26" viewBox="0 0 24 24"><path d="M6.6 10.8a15 15 0 006.6 6.6l2.2-2.2a1 1 0 011-.25 11.4 11.4 0 003.6.57 1 1 0 011 1V20a1 1 0 01-1 1A17 17 0 013 4a1 1 0 011-1h3.5a1 1 0 011 1c0 1.25.2 2.45.57 3.570a1 1 0 01-.25 1z" fill="#888"/></svg>
      <span>Call Us <strong>(262) 555-0147</strong></span>
    </div>
  </div>
</section>

<section class="card card--back" aria-label="Postcard back">
  <address class="return-address">
    <strong>BrightCoat Crew</strong>
    4389 Juniper Ave #7<br>Waukesha, WI 53947
  </address>

  <div class="indicia">Presorted<br>Standard<br>QMRB Postage<b>PAID</b>PMX</div>
  <div class="address-window"></div>

  <p class="intro">At BrightCoat Crew we stand apart with thorough communication and by catering the size of the crew to the size of your home to complete your project in two days or less. How do we do this? BrightCoat Crew offers this exceptional customer service through 5 key ways.</p>

  <ul class="values">
    <li><svg class="tick" viewBox="0 0 16 16"><rect x="1" y="3" width="11" height="11" fill="none" stroke="#222" stroke-width="1.5"/><path d="M4 8l3 3 8-9" fill="none" stroke="#222" stroke-width="2"/></svg>Quality Workmanship</li>
    <li><svg class="tick" viewBox="0 0 16 16"><rect x="1" y="3" width="11" height="11" fill="none" stroke="#222" stroke-width="1.5"/><path d="M4 8l3 3 8-9" fill="none" stroke="#222" stroke-width="2"/></svg>Organized Business Systems</li>
    <li><svg class="tick" viewBox="0 0 16 16"><rect x="1" y="3" width="11" height="11" fill="none" stroke="#222" stroke-width="1.5"/><path d="M4 8l3 3 8-9" fill="none" stroke="#222" stroke-width="2"/></svg>Thorough Communication</li>
    <li><svg class="tick" viewBox="0 0 16 16"><rect x="1" y="3" width="11" height="11" fill="none" stroke="#222" stroke-width="1.5"/><path d="M4 8l3 3 8-9" fill="none" stroke="#222" stroke-width="2"/></svg>Trust</li>
    <li><svg class="tick" viewBox="0 0 16 16"><rect x="1" y="3" width="11" height="11" fill="none" stroke="#222" stroke-width="1.5"/><path d="M4 8l3 3 8-9" fill="none" stroke="#222" stroke-width="2"/></svg>Timeliness</li>
  </ul>

  <div class="info">
    <svg width="30" height="30" viewBox="0 0 30 30"><circle cx="15" cy="15" r="12" fill="none" stroke="#777" stroke-width="2"/><circle cx="15" cy="9.5" r="1.6" fill="#777"/><path d="M15 13v9" stroke="#777" stroke-width="2.4"/></svg>
    <p>We cater the size of the crew to the size of the job and work full continuous days until the project is complete.</p>
  </div>

  <div class="back-band"></div>
  <div class="cta-tab">BOOK YOUR FREE ESTIMATE</div>
  <div class="band-row">
    <span class="band-brand">BrightCoat Crew</span>
    <span class="item">
      <svg width="18" height="18" viewBox="0 0 24 24"><path d="M6.6 10.8a15 15 0 006.6 6.6l2.2-2.2a1 1 0 011-.25 11.4 11.4 0 003.6.57 1 1 0 011 1V20a1 1 0 01-1 1A17 17 0 013 4a1 1 0 011-1h3.5a1 1 0 011 1c0 1.25.2 2.45.57 3.57a1 1 0 01-.25 1z" fill="#fff"/></svg>
      <b>(262) 555-0147</b>
    </span>
    <span class="dot"></span>
    <span class="item">
      <svg width="20" height="16" viewBox="0 0 22 18" class="icon--light"><rect x="1" y="1" width="20" height="16"/><path d="M1 1l10 8 10-8"/></svg>
      <span><b>office</b>@brightcoatcrew.example</span>
    </span>
    <span class="dot"></span>
    <span class="item">
      <svg width="18" height="18" viewBox="0 0 30 30" class="icon--light"><circle cx="15" cy="15" r="12"/><ellipse cx="15" cy="15" rx="5" ry="12"/><path d="M3 15h24"/></svg>
      <span>www.<b>BrightCoatCrew</b>.example</span>
    </span>
  </div>
</section>

</body>
</html>
```